Purl Haven planner/ book cover

PURL HAVEN" - A UNIQUE NOTEBOOK FOR CRAFTS. The main goal of a "Purl Haven" notebook is to arrange your crafts notes like knitting planner. Its pages are systematically structured, so they are easy to review, and all the information about the started project is in one place. The notebook has a click opening system, so you can remove, insert, change pages.
This is the old design in Latvian language. I want a new, classic, modern cover design for selling book in USA.I prefer original picture rather than download. Maybe for some of yourself drawings. Illustrated color-wash and minimalistic style better than photography.
Look at the pages inside design so that the lid fits. Maybe i want to change some clipart on the inside as well (just small one, like ball of yarn, sweater, can be seen in the picture, more classic style, not so childish, but that's latter), leave yoga clipart and the colors. Check please video.
https://www.examplevideo-host.com/watch?v=Qm4rT8zLk2W
www.purlhavenstudio.com its my style.

book title- purl haven
slogan- its time for sitting to do some knitting
size- 18 x 23,5 x 4 cm

Colors
d3a5cc
eea4c8
fdf2f7
fbd4d5
fdf0f6
ffffff
e34297
a64599
b868aa

```html
<!DOCTYPE html>
<html lang="en">
<head>
<meta charset="utf-8">
<title>Purl Haven – Planner Cover</title>
<link rel="stylesheet" href="https://fonts.googleapis.com/css2?family=Alex+Brush&family=Gelasio:wght@700&family=Gentium+Book+Plus&display=swap">
<style>
  :root {
    --backdrop: #b3b3b3;
    --paper: #ffffff;
    --ink: #111111;
    --gold: #d9a92a;
    --gold-light: #f1dc8c;
    --gold-wash: #f6e7a6;
    --blush: #f0a9a4;
    --blush-soft: #fbd4d5;
    --magenta: #b3237a;
    --magenta-light: #d04d9a;
  }
  * { margin: 0; padding: 0; box-sizing: border-box; }
  html, body { width: 1200px; height: 1200px; overflow: hidden; }
  body { background: var(--backdrop); position: relative; }

  .cover {
    position: absolute;
    left: 183px; top: 0;
    width: 834px; height: 1200px;
    background: var(--paper);
    overflow: hidden;
  }
  .cover__art { position: absolute; inset: 0; width: 100%; height: 100%; }

  .title {
    position: absolute;
    left: 0; right: 0;
    text-align: center;
    color: var(--ink);
  }
  .title__script {
    top: 250px;
    left: 70px;
    font-family: "Alex Brush", cursive;
    font-size: 220px;
    line-height: 1;
  }
  .title__main {
    top: 530px;
    left: 40px;
    font-family: "Gelasio", serif;
    font-weight: 700;
    font-size: 116px;
    line-height: 1;
    letter-spacing: 1px;
  }
  .slogan {
    position: absolute;
    left: 160px; width: 540px;
    top: 905px;
    text-align: center;
    font-family: "Gentium Book Plus", serif;
    font-size: 52px;
    line-height: 64px;
    color: var(--ink);
    white-space: nowrap;
  }
</style>
</head>
<body>
  <main class="cover">
    <svg class="cover__art" viewBox="0 0 834 1200" xmlns="http://www.w3.org/2000/svg">
      <defs>
        <radialGradient id="gold-wash-left" cx="0" cy="0" r="1">
          <stop offset="0" stop-color="var(--gold-light)"/>
          <stop offset="0.6" stop-color="var(--gold-wash)" stop-opacity="0.6"/>
          <stop offset="1" stop-color="var(--gold-wash)" stop-opacity="0"/>
        </radialGradient>
        <radialGradient id="gold-wash-right" cx="1" cy="0.1" r="1">
          <stop offset="0" stop-color="var(--gold-light)"/>
          <stop offset="0.6" stop-color="var(--gold-wash)" stop-opacity="0.6"/>
          <stop offset="1" stop-color="var(--gold-wash)" stop-opacity="0"/>
        </radialGradient>
        <linearGradient id="blush-stroke" x1="0" y1="0" x2="1" y2="0">
          <stop offset="0" stop-color="var(--blush-soft)" stop-opacity="0.7"/>
          <stop offset="0.5" stop-color="var(--blush)" stop-opacity="0.85"/>
          <stop offset="1" stop-color="var(--blush-soft)" stop-opacity="0.6"/>
        </linearGradient>
        <linearGradient id="knit-fabric" x1="0" y1="0" x2="1" y2="1">
          <stop offset="0" stop-color="var(--magenta)"/>
          <stop offset="1" stop-color="var(--magenta-light)"/>
        </linearGradient>
      </defs>

      <g role="img" aria-label="Soft gold watercolor wash in the top corners">
        <rect x="0" y="0" width="260" height="260" fill="url(#gold-wash-left)"/>
        <rect x="560" y="0" width="274" height="330" fill="url(#gold-wash-right)"/>
      </g>

      <path role="img" aria-label="Blush pink watercolor brush stroke behind the title"
            d="M0 340 C200 270 500 240 834 250 L834 560 C650 600 430 630 250 690 C160 700 80 660 0 620 Z"
            fill="url(#blush-stroke)"/>

      <g fill="none" stroke="var(--gold)" stroke-width="2.5">
        <polygon points="418,108 708,282 778,540 582,820 160,688 66,418 188,248"/>
        <polygon points="262,132 688,200 732,470 598,800 400,848 150,690 96,420" stroke-opacity="0.75"/>
      </g>

      <path role="img" aria-label="Photo of magenta knitting on needles"
            d="M0 830 C50 838 100 846 135 852 C140 940 142 1020 150 1100 C300 1120 430 1110 560 1090 C680 1072 760 1062 834 1058 L834 1200 L0 1200 Z"
            fill="url(#knit-fabric)"/>
    </svg>

    <div class="title title__script">Purl</div>
    <div class="title title__main">Haven</div>
    <p class="slogan">Its time for sitting to<br>do some knitting</p>
  </main>
</body>
</html>
```